Verpackungskonzept für Nusskerne, Nussöl, Nussmus
Zielgruppe
Unser Unternehmen stellt verschiedenste Produkte aus Nüssen her.
Unsere Vertriebskanäle sind der gehobene Einzelhandel, sowie direkter Onlinevertrieb.
Unsere Zielgruppe sind umweltbewusste Konsumenten die Wert auf Natürlichkeit,
Nachhaltigkeit und Persönlichkeit/Herzlichkeit legen.
Aufgabenstellung
Für unser Rohwarensortiment (Nusskerne, Nussöl, Nussmus) suchen wir ein Verpackungskonzept und streben eine langfristige Dienstleisterbeziehung (Folgeaufträge) an.
Um Ihnen möglichst wenig unnötige Arbeit zu verursachen, erwarten wir in einem ersten Schritt grobe Konzepte, die im weiteren Verlauf im Detail ausgearbeitet werden.
Ihre Entwürfe sollten folgende Vorgaben erfüllen:
- Berücksichtigen Sie zwei verschiedene Nusssorten als Referenz (Macadamia und Walnuss)
- Berücksichtigen Sie eine visuell einfache Unterscheidung der Nusssorten
- Erstellen Sie bitte Konzepte für
- Öl (Glasflasche 100ml siehe Anhang)
- Nussmus (Glas 250g siehe Anhang)
- Nusskerne (freie Verpackungswahl)
- Berücksichtigen Sie unser Logo (Anhang)
Der Textinhalt ist für die Konzeptausarbeitung nicht relevant.
Bei Rückfragen gerne und jeder Zeit melden.
Herzlichen Dank für Ihre kreativen Vorschläge!

```html
<!DOCTYPE html>
<html lang="de">
<head>
<meta charset="utf-8">
<title>NORVELA – Verpackungskonzept Macadamia &amp; Walnuss</title>
<link rel="stylesheet" href="https://fonts.googleapis.com/css2?family=Archivo+Black&family=Cinzel:wght@400&family=Dancing+Script:wght@500&family=Rubik:wght@700;800&display=swap">
<style>
  :root{
    --stage:#8e8e8e;
    --kraft:#dac59e;
    --cream:#efe3c8;
    --macadamia:#d3262a;
    --walnut:#3fae2c;
    --brand-grey:#7b7a78;
    --ink-brown:#6a2812;
    --white:#ffffff;
    --mark:#2b2b2b;
  }
  *{box-sizing:border-box;margin:0;padding:0}
  html,body{width:1200px;height:546px;overflow:hidden}
  body{background:var(--stage);position:relative;font-family:"Rubik",sans-serif}

  .variant{--accent:var(--macadamia);--photo:linear-gradient(120deg,#8a5a36 0%,#b9906a 55%,#cdb38c 100%)}
  .variant.is-walnut{--accent:var(--walnut);--photo:linear-gradient(120deg,#9a5e2e 0%,#c08552 55%,#cfa77a 100%)}

  .photo{position:absolute;background:var(--photo);border-radius:6px}
  .brand-dot{position:absolute;left:50%;transform:translateX(-50%);border-radius:50%;background:var(--mark)}

  /* Nusskerne – Standbeutel */
  .pouch{position:absolute;top:125px;width:213px;height:313px;background:var(--kraft);border-radius:3px 3px 10px 10px;overflow:hidden}
  .pouch__top{position:absolute;inset:0 0 auto 0;height:62px;background:var(--accent)}
  .pouch .brand-dot{top:18px;width:32px;height:32px}
  .pouch__name{position:absolute;top:60px;width:100%;text-align:center;font-family:"Cinzel",serif;font-size:20px;line-height:26px;color:var(--brand-grey);letter-spacing:1px}
  .pouch__claim{position:absolute;top:100px;left:10px;font-family:"Dancing Script",cursive;font-size:12px;color:var(--ink-brown);transform:rotate(-16deg);transform-origin:left bottom}
  .pouch .photo{top:108px;left:62px;width:140px;height:76px}
  .pouch__label{position:absolute;top:190px;left:27px;width:170px;height:42px;background:var(--accent);color:var(--white);font-weight:800;font-size:22px;display:flex;align-items:center;justify-content:center}
  .pouch__slogan{position:absolute;top:256px;width:100%;text-align:center;font-family:"Archivo Black",sans-serif;font-size:18px;line-height:23px;color:var(--ink-brown)}

  /* Nussöl – Flaschenetikett */
  .bottle-label{position:absolute;top:110px;width:77px;height:137px;background:var(--cream);overflow:hidden}
  .bottle-label__top{height:16px;background:var(--accent)}
  .bottle-label .brand-dot{top:24px;width:14px;height:14px}
  .bottle-label__name{position:absolute;top:42px;width:100%;text-align:center;font-family:"Cinzel",serif;font-size:9px;color:var(--brand-grey)}
  .bottle-label__claim{position:absolute;top:58px;left:4px;width:20px;font-family:"Dancing Script",cursive;font-size:6px;line-height:7px;color:var(--ink-brown);transform:rotate(-12deg)}
  .bottle-label .photo{top:64px;left:26px;width:46px;height:32px;border-radius:4px}
  .bottle-label__band{position:absolute;top:102px;left:8px;width:64px;height:22px;background:var(--accent);color:var(--white);font-size:9.5px;font-weight:800;display:flex;align-items:center;justify-content:center;transform:rotate(-4deg)}

  /* Nussmus – Deckel & Glasetikett */
  .jar-lid{position:absolute;top:314px;width:140px;height:40px;border-radius:50%;background:var(--cream);overflow:hidden}
  .jar-lid__name{position:absolute;top:4px;width:100%;text-align:center;font-family:"Cinzel",serif;font-size:6px;color:var(--brand-grey)}
  .jar-lid .photo{top:13px;left:48px;width:44px;height:11px;border-radius:3px}
  .jar-lid__band{position:absolute;top:27px;left:34px;width:72px;height:7px;background:var(--accent);color:var(--white);font-size:5px;font-weight:700;text-align:center;line-height:7px}
  .jar-label{position:absolute;top:380px;width:142px;height:93px;background:var(--cream);overflow:hidden}
  .jar-label__claim{position:absolute;top:20px;left:6px;width:32px;font-family:"Dancing Script",cursive;font-size:7px;line-height:8px;color:var(--ink-brown);transform:rotate(-10deg)}
  .jar-label .photo{top:22px;left:42px;width:92px;height:34px;border-radius:4px}
  .jar-label__band{position:absolute;top:60px;left:-4px;width:150px;height:26px;background:var(--accent);color:var(--white);font-size:14px;font-weight:800;display:flex;align-items:center;justify-content:center;transform:rotate(-5deg)}
</style>
</head>
<body>

<section class="variant">
  <div class="pouch" style="left:97px">
    <div class="pouch__top"></div>
    <span class="brand-dot"></span>
    <div class="pouch__name">NORVELA</div>
    <div class="photo" role="img" aria-label="Foto: geknackte Macadamianüsse mit Blatt"></div>
    <div class="pouch__claim">gesund knabern</div>
    <div class="pouch__label">Macadamia</div>
    <div class="pouch__slogan">DIREKT AUS<br>DER NATUR</div>
  </div>

  <div class="bottle-label" style="left:503px">
    <div class="bottle-label__top"></div>
    <span class="brand-dot"></span>
    <div class="bottle-label__name">NORVELA</div>
    <div class="bottle-label__claim">direkt aus der Natur</div>
    <div class="photo" role="img" aria-label="Foto: Macadamianüsse"></div>
    <div class="bottle-label__band">Macadamiaöl</div>
  </div>

  <div class="jar-lid" style="left:429px">
    <div class="jar-lid__name">NORVELA</div>
    <div class="photo" role="img" aria-label="Foto: Macadamianüsse"></div>
    <div class="jar-lid__band">Macadamiamus</div>
  </div>
  <div class="jar-label" style="left:427px">
    <div class="jar-label__claim">direkt aus der Natur</div>
    <div class="photo" role="img" aria-label="Foto: Macadamianüsse mit Blatt"></div>
    <div class="jar-label__band">Macadamiamus</div>
  </div>
</section>

<section class="variant is-walnut">
  <div class="pouch" style="left:701px">
    <div class="pouch__top"></div>
    <span class="brand-dot"></span>
    <div class="pouch__name">NORVELA</div>
    <div class="photo" role="img" aria-label="Foto: Walnusskerne und Walnussschale mit Blättern"></div>
    <div class="pouch__claim">gesund knabern</div>
    <div class="pouch__label">Walnuss</div>
    <div class="pouch__slogan">DIREKT AUS<br>DER NATUR</div>
  </div>

  <div class="bottle-label" style="left:1103px">
    <div class="bottle-label__top"></div>
    <span class="brand-dot"></span>
    <div class="bottle-label__name">NORVELA</div>
    <div class="bottle-label__claim">direkt aus der Natur</div>
    <div class="photo" role="img" aria-label="Foto: Walnüsse mit Blatt"></div>
    <div class="bottle-label__band">Walnussöl</div>
  </div>

  <div class="jar-lid" style="left:1025px">
    <div class="jar-lid__name">NORVELA</div>
    <div class="photo" role="img" aria-label="Foto: Walnüsse"></div>
    <div class="jar-lid__band">Walnussmus</div>
  </div>
  <div class="jar-label" style="left:1023px">
    <div class="jar-label__claim">direkt aus der Natur</div>
    <div class="photo" role="img" aria-label="Foto: Walnusskerne mit Blatt"></div>
    <div class="jar-label__band">Walnussmus</div>
  </div>
</section>

</body>
</html>
```